Design of a User Interface for a Kids Educational Game

User interface design for kids educational games - design should be simple, modern and elegant, but still pleasing to children. Not too many graphics, or if any, then such which can be reused. Please everything as a mockup in some vector graphics format (compatible with SVG).

See the screenshots and slides attached to know exactly what needs to be styled. You don't need to style everything in the beginning, just style one typical slide first, and I will notify those who have better designs, they can then refine this until we find a winner (so you don't waste too much of your time).

Typical game input on one app screen is very simple:

1+2=_
Next >
===============
A (Apple)
Next >
===============

best regards,

Tobias

```html
<!DOCTYPE html>
<html lang="en">
<head>
<meta charset="utf-8">
<title>Counting Game – Number Pick</title>
<link rel="stylesheet" href="https://fonts.googleapis.com/css2?family=Open+Sans:wght@700&display=swap">
<style>
  :root {
    --field-green: #b2d235;
    --art-yellow: #fec40f;
    --art-yellow-soft: #f3cd2c;
    --tile-red: #e91e4f;
    --tile-yellow: #fec40f;
    --tile-green: #0c9547;
    --button-red: #e91e4f;
    --button-edge: #b8173e;
    --digit-white: #ffffff;
  }
  * { margin: 0; padding: 0; box-sizing: border-box; }
  html, body { width: 1200px; height: 900px; overflow: hidden; }
  body { background: var(--field-green); font-family: "Open Sans", Arial, sans-serif; }
  .game-screen { position: relative; width: 1200px; height: 900px; background: var(--field-green); }
  .hero-art {
    position: absolute; left: 100px; top: 213px;
    width: 467px; height: 477px;
    border-radius: 32px;
    background: radial-gradient(circle at 45% 48%, var(--art-yellow) 0%, var(--art-yellow-soft) 60%, var(--field-green) 100%);
  }
  .answer-tile {
    position: absolute;
    width: 202px; height: 202px;
    border-radius: 26px;
    display: flex; align-items: center; justify-content: center;
    color: var(--digit-white);
    font-weight: 700; font-size: 196px; line-height: 1;
  }
  .answer-tile span { display: block; transform: translateY(-4px); }
  .tile-one   { left: 707px; top: 92px;  background: var(--tile-red);    transform: rotate(-3deg); }
  .tile-two   { left: 900px; top: 300px; background: var(--tile-yellow); transform: rotate(4deg); }
  .tile-three { left: 707px; top: 518px; background: var(--tile-green);  transform: rotate(-3deg); }
  .next-button {
    position: absolute; left: 936px; top: 726px;
    width: 218px; height: 128px;
    border: none; border-radius: 36px;
    background: var(--button-red);
    box-shadow: 0 12px 0 var(--button-edge);
    display: flex; align-items: center; justify-content: center;
    cursor: pointer;
  }
  .next-button svg { width: 130px; height: 70px; }
</style>
</head>
<body>
  <main class="game-screen">
    <div class="hero-art" role="img" aria-label="Illustration of a yellow ball with a red star casting a soft shadow"></div>

    <div class="answer-tile tile-one"><span>1</span></div>
    <div class="answer-tile tile-two"><span>2</span></div>
    <div class="answer-tile tile-three"><span>3</span></div>

    <button class="next-button" aria-label="Next">
      <svg viewBox="0 0 130 70" aria-hidden="true">
        <path d="M12 35 H108 M80 9 L112 35 L80 61" fill="none" stroke="var(--digit-white)"
              stroke-width="15" stroke-linecap="round" stroke-linejoin="round"/>
      </svg>
    </button>
  </main>
</body>
</html>
```